The calm within me tour 2019

I need an improvement of my own design for a speaking tour on shame and mental health. The advertisement will be for social media. I would like someone to remove the background and do something creative and contemporary. My preference is just my head and shoulders.

Target Market(s)

Church pastors and leaders of mental health organisations

Industry/Entity Type

Mental Health

Requirements
Must have
• The same wording as original
• Delete background and replace with something that is simple but funky

```html
<!DOCTYPE html>
<html lang="en">
<head>
<meta charset="utf-8">
<title>The Calm Within Me Tour 2019</title>
<link rel="stylesheet" href="https://fonts.googleapis.com/css2?family=Arimo:wght@400;700&display=swap">
<style>
  :root {
    --bg-blue: #5a78f2;
    --bg-blue-light: #6d88f6;
    --bg-blue-deep: #4e69ea;
    --disc-blue: #4f6cff;
    --ink-white: #ffffff;
    --tag-grey: #46474d;
    --photo-dark: #2a2c36;
    --photo-mid: #6b5f5a;
  }
  * { margin: 0; padding: 0; box-sizing: border-box; }
  html, body { width: 1200px; height: 564px; overflow: hidden; }
  body { font-family: "Arimo", Arial, sans-serif; }

  .tour-banner {
    position: relative;
    width: 1200px;
    height: 564px;
    overflow: hidden;
    background:
      radial-gradient(ellipse 60% 40% at 30% 20%, var(--bg-blue-light), transparent 70%),
      radial-gradient(ellipse 50% 50% at 80% 80%, var(--bg-blue-deep), transparent 70%),
      var(--bg-blue);
  }
  .backdrop-texture { position: absolute; inset: 0; }

  .title-disc {
    position: absolute;
    left: 132px;
    top: 48px;
    width: 474px;
    height: 474px;
    border-radius: 50%;
    background: var(--disc-blue);
    opacity: 0.85;
  }

  .tour-title {
    position: absolute;
    left: 0;
    top: 0;
    color: var(--ink-white);
    font-weight: 700;
    text-shadow: 0 2px 6px rgba(0,0,0,0.18);
    letter-spacing: -0.02em;
  }
  .tour-title span { position: absolute; white-space: nowrap; line-height: 1; }
  .title-the { left: 262px; top: 80px; font-size: 70px; }
  .title-calm { left: 192px; top: 146px; font-size: 94px; }
  .title-within { left: 200px; top: 266px; font-size: 58px; }
  .title-me { left: 388px; top: 206px; font-size: 140px; }

  .tour-year {
    position: absolute;
    left: 244px;
    top: 330px;
    width: 290px;
    height: 122px;
    background: var(--tag-grey);
    transform: rotate(-3deg);
    display: flex;
    align-items: center;
    justify-content: center;
    color: var(--ink-white);
    font-weight: 700;
    font-size: 104px;
    letter-spacing: -0.01em;
  }

  .speaker-portrait {
    position: absolute;
    left: 672px;
    top: 68px;
    width: 416px;
    height: 496px;
    border-radius: 160px 160px 0 0;
    background: linear-gradient(180deg, var(--photo-mid) 0%, var(--photo-mid) 38%, var(--photo-dark) 52%, var(--photo-dark) 100%);
  }

  .speaker-name {
    position: absolute;
    right: 40px;
    top: 58px;
    display: flex;
    flex-direction: column;
    align-items: center;
    gap: 12px;
    color: var(--ink-white);
  }
  .speaker-name .name-dot {
    width: 84px;
    height: 84px;
    border-radius: 50%;
    background: var(--ink-white);
  }
  .speaker-name .name-text {
    font-weight: 400;
    font-size: 26px;
    line-height: 1;
  }
</style>
</head>
<body>
  <main class="tour-banner">
    <svg class="backdrop-texture" width="1200" height="564" viewBox="0 0 1200 564" aria-hidden="true">
      <path d="M0 120 C200 80 400 180 600 130 S1000 60 1200 110" fill="none" stroke="#6a86f5" stroke-width="28" opacity="0.35"/>
      <path d="M0 430 C220 470 420 380 640 440 S1000 500 1200 450" fill="none" stroke="#4c67e8" stroke-width="34" opacity="0.35"/>
    </svg>

    <div class="title-disc"></div>

    <h1 class="tour-title" aria-label="The Calm within me">
      <span class="title-the">The</span>
      <span class="title-calm">Calm</span>
      <span class="title-within">within</span>
      <span class="title-me">me</span>
    </h1>

    <div class="tour-year">2019</div>

    <div class="speaker-portrait" role="img" aria-label="Head-and-shoulders photo of the speaker in a black V-neck t-shirt"></div>

    <div class="speaker-name">
      <span class="name-dot"></span>
      <span class="name-text">dan fellows</span>
    </div>
  </main>
</body>
</html>
```